Ferncrest Dental, LLC business card project

Business card to be designed with current logo.
Dental office- please keep design of card that looks clean and professional.
Please include the following info:
Ferncrest Dental, LLC
Dr. Lorna Pettigrew
2871 Marlowe Street
Bethlehem, PA 18093
610-555-0193
ferncrestdental.office@examplemail.test
Hello everyone-
Reason: Just got back from overseas- will look at all designs and provide feedback. Thank you!
Reason: Polling my friends for the final selection-
thank you to all those that participated- so many talented designers!

```html
<!DOCTYPE html>
<html lang="en">
<head>
<meta charset="utf-8">
<title>Ferncrest Dental, LLC — Business Card</title>
<link href="https://fonts.googleapis.com/css2?family=Source+Sans+3:wght@400;600;700&display=swap" rel="stylesheet">
<style>
  :root {
    --green: #6a9f3a;
    --green-dark: #5a9132;
    --green-pale: #e8f0d2;
    --text: #2f2f2f;
    --bleed: #a9d7e8;
    --crop: #222;
    --paper: #ffffff;
  }
  * { box-sizing: border-box; margin: 0; padding: 0; }
  html, body {
    width: 1000px; height: 1200px; overflow: hidden;
    background: var(--paper);
    font-family: "Source Sans 3", "Myriad Pro", Arial, sans-serif;
    color: var(--text);
  }
  .sheet { position: relative; width: 1000px; height: 1200px; }

  .card-slot { position: absolute; left: 140px; width: 720px; height: 412px; }
  .card-slot--front { top: 120px; }
  .card-slot--back { top: 660px; }

  .card {
    position: absolute; inset: 0; overflow: hidden;
    background: var(--paper);
    outline: 1.5px solid var(--bleed);
    outline-offset: 6px;
  }
  .card--back { background: var(--green-pale); }

  .side-label {
    position: absolute; right: -14px; top: 432px;
    font-size: 19px; font-weight: 600; letter-spacing: 0.5px; color: #111;
  }

  .crop { position: absolute; background: var(--crop); }
  .crop--h { width: 30px; height: 1.5px; }
  .crop--v { width: 1.5px; height: 30px; }
  .crop--tl-h { left: -42px; top: 0; }
  .crop--tl-v { left: 0; top: -42px; }
  .crop--tr-h { right: -42px; top: 0; }
  .crop--tr-v { right: 0; top: -42px; }
  .crop--bl-h { left: -42px; bottom: 0; }
  .crop--bl-v { left: 0; bottom: -42px; }
  .crop--br-h { right: -42px; bottom: 0; }
  .crop--br-v { right: 0; bottom: -42px; }

  .landscape { position: absolute; left: 0; top: 0; width: 720px; height: 412px; }

  /* Front */
  .brand {
    position: absolute; top: 40px; left: 0; right: 0;
    text-align: center;
    font-size: 58px; font-weight: 400; color: var(--green);
    letter-spacing: -0.5px; line-height: 1;
  }

  .contact { position: absolute; top: 160px; left: 40px; right: 0; text-align: center; }
  .contact__name { font-size: 33px; font-weight: 700; color: var(--text); margin-bottom: 14px; line-height: 1.1; }
  .contact__line { font-size: 23px; line-height: 34px; }
  .contact__label { font-size: 15px; font-weight: 600; color: var(--green); letter-spacing: 0.5px; margin-right: 6px; }

  .address {
    position: absolute; top: 354px; left: 40px; right: 0; text-align: center;
    font-size: 23px; color: #fff;
  }

  /* Back */
  .appointment__title {
    position: absolute; top: 62px; left: 0; right: 0; text-align: center;
    font-size: 25px; font-weight: 700; color: var(--green); letter-spacing: 0.3px;
  }
  .appointment__field {
    position: absolute; left: 160px; width: 388px;
    display: flex; align-items: flex-end; gap: 10px;
    font-size: 18px; font-weight: 700; color: var(--green);
  }
  .appointment__field--date { top: 150px; }
  .appointment__field--time { top: 228px; }
  .appointment__rule { flex: 1; height: 1.5px; background: var(--green); margin-bottom: 5px; }
</style>
</head>
<body>
<main class="sheet">

  <section class="card-slot card-slot--front" aria-label="Business card front">
    <span class="crop crop--h crop--tl-h"></span><span class="crop crop--v crop--tl-v"></span>
    <span class="crop crop--h crop--tr-h"></span><span class="crop crop--v crop--tr-v"></span>
    <span class="crop crop--h crop--bl-h"></span><span class="crop crop--v crop--bl-v"></span>
    <span class="crop crop--h crop--br-h"></span><span class="crop crop--v crop--br-v"></span>

    <div class="card card--front">
      <p class="brand">Ferncrest Dental, LLC</p>

      <div class="contact">
        <p class="contact__name">Dr. Lorna Pettigrew</p>
        <p class="contact__line"><span class="contact__label">TEL</span>610-555-0193</p>
        <p class="contact__line"><span class="contact__label">EMAIL</span>ferncrestdental.office@examplemail.test</p>
      </div>

      <svg class="landscape" viewBox="0 0 720 412" role="img" aria-label="Green hillside with trees illustration">
        <path d="M0 330 C 180 300, 420 284, 720 298 L 720 412 L 0 412 Z" fill="var(--green-dark)"/>
      </svg>

      <p class="address">2871 Marlowe Street, Bethlehem, PA 18093</p>
    </div>
    <span class="side-label">FRONT</span>
  </section>

  <section class="card-slot card-slot--back" aria-label="Business card back">
    <span class="crop crop--h crop--tl-h"></span><span class="crop crop--v crop--tl-v"></span>
    <span class="crop crop--h crop--tr-h"></span><span class="crop crop--v crop--tr-v"></span>
    <span class="crop crop--h crop--bl-h"></span><span class="crop crop--v crop--bl-v"></span>
    <span class="crop crop--h crop--br-h"></span><span class="crop crop--v crop--br-v"></span>

    <div class="card card--back">
      <h2 class="appointment__title">NEXT APPOINTMENT</h2>
      <div class="appointment__field appointment__field--date"><span>DATE:</span><span class="appointment__rule"></span></div>
      <div class="appointment__field appointment__field--time"><span>TIME:</span><span class="appointment__rule"></span></div>

      <svg class="landscape" viewBox="0 0 720 412" role="img" aria-label="Pale hillside with trees illustration">
        <path d="M0 412 L 0 380 C 200 352, 460 338, 720 346 L 720 412 Z" fill="#fff"/>
      </svg>
    </div>
    <span class="side-label">BACK</span>
  </section>

</main>
</body>
</html>
```